Business card for a young aspring actress

My daughter is 18 and just starting out on her profession as an actress. She is a member of the Open Stage Company and has already had some extras work and a featured role in an upcoming Feature film.

She wants/needs a card that she can have to hand to give to those she comes into contact with in the theatre, TV and film industries.

We are thinking that it may be double sided with an impact side including a picture of her and her name etc with the reverse holding contact and other details.

She wants to go by the name Maren Joy Whitcombe.

She has done a little modelling but sees herself as an actress.

She can be seen in this video
http://www.hollybankacademy.example/videos/a3f19c7d5e2b8406c1d9e7f2a4b60835?width=640&height=480

Target Market(s)

Anyone she comes into contact with in theatre TV and film industries.

Industry/Entity Type

Business

Requirements
Nice to have
• She has email and a website www.marenwhitcombe.example She is quite a connected girl

```html
<!DOCTYPE html>
<html lang="en">
<head>
<meta charset="utf-8">
<title>Maren Joy Whitcombe – Business Card</title>
<link rel="stylesheet" href="https://fonts.googleapis.com/css2?family=Jura:wght@400;500&display=swap">
<style>
  :root {
    --page: #e9e6df;
    --card-black: #050505;
    --card-black-soft: #1c1c1c;
    --gold: #c9a24a;
    --grey-light: #9a9a9a;
    --grey-dark: #4f4f4f;
    --photo-light: #e4e8ea;
    --photo-mid: #a9aeb1;
    --photo-dark: #3a3c3e;
  }
  * { box-sizing: border-box; margin: 0; padding: 0; }
  html, body {
    width: 1200px;
    height: 1000px;
    overflow: hidden;
    background: var(--page);
    font-family: "Jura", "Segoe UI", sans-serif;
  }
  .sheet {
    position: relative;
    width: 1200px;
    height: 1000px;
  }
  .card {
    position: absolute;
    top: 190px;
    width: 440px;
    height: 620px;
    overflow: hidden;
    box-shadow: 0 10px 30px rgba(0,0,0,0.25);
  }

  /* Front side */
  .card--front {
    left: 120px;
    border-radius: 210px 0 210px 0;
    background: linear-gradient(180deg, var(--grey-light) 0%, var(--grey-dark) 100%);
  }
  .front__portrait {
    position: absolute;
    left: 0;
    top: 0;
    width: 360px;
    height: 620px;
    border-radius: 210px 0 190px 0;
    background:
      radial-gradient(ellipse 55% 40% at 45% 45%, var(--photo-light) 0%, var(--photo-mid) 60%, transparent 100%),
      linear-gradient(90deg, var(--photo-dark) 0%, var(--photo-mid) 30%, var(--photo-light) 55%, var(--photo-mid) 80%, var(--photo-dark) 100%);
  }
  .name-block {
    position: absolute;
    background: var(--card-black);
    color: var(--gold);
    font-weight: 400;
    font-size: 25px;
    line-height: 1.18;
    letter-spacing: 4px;
    text-transform: uppercase;
  }
  .card--front .name-block {
    left: 22px;
    bottom: 48px;
    padding: 14px 18px 14px 22px;
  }

  /* Back side */
  .card--back {
    left: 640px;
    border-radius: 0 230px 0 0;
    background: linear-gradient(160deg, var(--card-black-soft) 0%, var(--card-black) 40%, var(--card-black) 100%);
  }
  .card--back .name-block {
    left: 32px;
    top: 96px;
    background: none;
  }
  .back__contact {
    position: absolute;
    right: 36px;
    bottom: 48px;
    list-style: none;
    text-align: right;
    color: var(--gold);
    font-size: 19px;
    font-weight: 500;
    line-height: 2;
    letter-spacing: 1px;
  }
</style>
</head>
<body>
<main class="sheet">
  <section class="card card--front" aria-label="Card front">
    <div class="front__portrait" role="img" aria-label="Black and white portrait photograph of the actress, hands resting at her cheek"></div>
    <h1 class="name-block">Maren<br>Joy<br>Whitcombe</h1>
  </section>

  <section class="card card--back" aria-label="Card back">
    <h2 class="name-block">Maren<br>Joy<br>Whitcombe</h2>
    <ul class="back__contact">
      <li>+44 7700 900142</li>
      <li>+44 7700 900187</li>
      <li>maren@marenwhitcombe.example</li>
      <li>www.marenwhitcombe.example</li>
    </ul>
  </section>
</main>
</body>
</html>
```